Physical Large Banner For Corporate Event

Hi, we would like a large banner designed for a corporate event using adobe illustrator/pdf. The size of the banner must be 2000 (h)x800 (w) mm to fit with the printing requirements (please visit https://www.inkvaleprints.com/products/48/banner-stands and see the guidelines for size for a standard banner)

Our organisation holds events for students to find out more on top careers such as Investment Banking & Law. The banner design can be fairly simple but bold using the same themes and colours on our website www.brightlanefutures.co.uk. We can provide imagery of our logo for use/other pictures requested such as those for students/cityscapes etc.

The only text on the banner should be our web address at the bottom (www.brightlanefutures.co.uk) and a line that says "A Head Start in the City, We bring the internship to you..." like in our website homepage.

Target Market(s)

Students & Graduate Recruiters

Industry/Entity Type

Education

Requirements
Must have
• Website address
• Cool imagery
Should not have
• Too much clutter, clean and simple pleaseE

```html
<!DOCTYPE html>
<html lang="en">
<head>
<meta charset="utf-8">
<title>BrightLane – Event Banner</title>
<link href="https://fonts.googleapis.com/css2?family=Montserrat:wght@400;600;800&display=swap" rel="stylesheet">
<style>
  :root {
    --paper: #ffffff;
    --navy: #1b2757;
    --navy-deep: #141d45;
    --sky-blue: #3561a3;
    --glass-blue: #1f3d70;
    --glass-deep: #16294d;
    --city-gold: #f0b54a;
    --city-amber: #d98b2b;
    --brand-grey: #5a5a5c;
    --brand-red: #8e1b1f;
    --brand-red-deep: #6e1215;
    --text-light: #ffffff;
  }
  * { margin: 0; padding: 0; box-sizing: border-box; }
  html, body { width: 1200px; height: 3000px; overflow: hidden; background: var(--paper); }
  .banner {
    position: relative;
    width: 1200px;
    height: 3000px;
    font-family: "Montserrat", sans-serif;
    background: var(--paper);
    overflow: hidden;
  }
  .brand-header {
    position: absolute;
    top: 0; left: 0;
    width: 1200px; height: 492px;
    background: var(--paper);
    display: flex;
    align-items: center;
    justify-content: center;
    gap: 28px;
  }
  .brand-mark {
    width: 58px; height: 58px;
    background: var(--brand-red);
  }
  .brand-name {
    font-weight: 600;
    font-size: 104px;
    letter-spacing: 1px;
    color: var(--brand-grey);
  }
  .headline-panel {
    position: absolute;
    top: 492px; left: 0;
    width: 1200px; height: 960px;
    background: var(--navy);
  }
  .city-photo {
    position: absolute;
    top: 1440px; left: 0;
    width: 1200px; height: 1340px;
    background:
      radial-gradient(ellipse 38% 22% at 45% 90%, rgba(240,181,74,0.85), transparent 75%),
      radial-gradient(ellipse 22% 14% at 88% 88%, rgba(217,139,43,0.6), transparent 75%),
      radial-gradient(ellipse 16% 40% at 6% 62%, rgba(240,181,74,0.7), transparent 75%),
      radial-gradient(ellipse 14% 22% at 55% 52%, rgba(240,181,74,0.55), transparent 75%),
      radial-gradient(ellipse 20% 26% at 82% 60%, rgba(240,200,120,0.45), transparent 75%),
      linear-gradient(180deg, var(--navy) 0%, var(--sky-blue) 22%, var(--glass-blue) 48%, var(--glass-deep) 75%, #2a2c38 100%);
  }
  .headline {
    position: absolute;
    inset: 0;
    color: var(--text-light);
    font-weight: 800;
    text-transform: uppercase;
    line-height: 1;
    pointer-events: none;
  }
  .headline-line {
    position: absolute;
    left: 100px;
    display: block;
    white-space: nowrap;
  }
  .headline-line--1 { top: 549px;  font-size: 134px; }
  .headline-line--2 { top: 691px;  font-size: 134px; }
  .headline-line--3 { top: 959px;  font-size: 133px; }
  .headline-line--4 { top: 1094px; font-size: 161px; }
  .headline-line--5 { top: 1246px; font-size: 215px; }
  .footer-band {
    position: absolute;
    top: 2780px; left: 0;
    width: 1200px; height: 220px;
    background: linear-gradient(180deg, var(--brand-red) 0%, var(--brand-red-deep) 100%);
    display: flex;
    align-items: center;
    justify-content: center;
  }
  .web-address {
    color: var(--text-light);
    font-weight: 400;
    font-size: 62px;
    letter-spacing: 1px;
  }
</style>
</head>
<body>
  <div class="banner">
    <header class="brand-header">
      <span class="brand-mark" aria-hidden="true"></span>
      <span class="brand-name">BrightLane</span>
    </header>

    <section class="headline-panel"></section>

    <div class="city-photo" role="img" aria-label="Night cityscape of lit glass office towers with golden light trails on curving roads"></div>

    <h1 class="headline">
      <span class="headline-line headline-line--1">A Head Start</span>
      <span class="headline-line headline-line--2">In the City,</span>
      <span class="headline-line headline-line--3">We Bring the</span>
      <span class="headline-line headline-line--4">Internship</span>
      <span class="headline-line headline-line--5">To You...</span>
    </h1>

    <footer class="footer-band">
      <span class="web-address">www.brightlanefutures.co.uk</span>
    </footer>
  </div>
</body>
</html>
```